Banner Design for Holistic Clinic

We need a banner to be designed for a Holistic Clinic which treats patient using IV Nutrition therapy, IV Vitamin C therapy, Chelation therapy, Homoepathy , Accupuncture, Ayurveda. Our website is www.verdantcarehub.in

We need the banner to show case all our services. IV Nutrition therapy, IV Vitamin C therapy, Chelation therapy, Homoepathy , Accupuncture, Ayurveda with special emphasis on IV Therapies. This will be in the front of the web page and will be used for leaflets and flex material.Ideally

I like the concept of IV infsuion bags, fruits etc. I have attached some of the pic which i liked. Please see the attachment "banner clinic july 13" But feel free to change it and bring in something better that will showcase all our services together

Target Market(s)

30 plus Adults

Industry/Entity Type

Health And Wellness

Font styles to use
Serif

Colors
acd036
f37122
33a6d7

Requirements
Must have
• Some samples are given below. It got to be colourful, yet pleasing.

```html
<!DOCTYPE html>
<html lang="en">
<head>
<meta charset="utf-8">
<title>Verdant Care Hub</title>
<link href="https://fonts.googleapis.com/css2?family=Josefin+Sans:wght@300;400;600;700&family=Josefin+Slab:wght@400;600;700&display=swap" rel="stylesheet">
<style>
:root{
  --green:#2a8c3a;
  --green-dark:#1d7a30;
  --green-deep:#17692a;
  --lime:#8cc63f;
  --red:#d9262c;
  --text:#555;
  --label:#2d5e2a;
  --gray:#eeeeee;
  --white:#fff;
  --serif:'Josefin Slab',serif;
}
*{margin:0;padding:0;box-sizing:border-box}
html,body{width:1200px;height:2619px;overflow:hidden}
body{font-family:'Josefin Sans',sans-serif;color:var(--text);background:var(--white);position:relative}
ul{list-style:none}
.wrap{width:692px;margin:0 auto;position:relative;height:100%}
section,header,footer{position:relative;overflow:hidden}
h2,h3,h4,.brand-name,.hero-label{font-family:var(--serif)}

/* header */
.site-header{height:94px}
.brand{position:absolute;left:0;top:6px;display:flex;align-items:center;gap:8px}
.brand-mark{width:40px;height:40px;background:var(--green)}
.brand-doctor{font-size:7px;color:var(--text);font-weight:600;margin-bottom:2px}
.brand-name{font-size:18px;font-weight:700;color:var(--green);letter-spacing:.3px}
.brand-tag{font-size:6px;color:var(--text);margin-top:2px}
.header-phone{position:absolute;right:0;top:14px;display:flex;align-items:center;gap:8px;font-size:15px;color:#333}
.phone-box{width:24px;height:24px;background:var(--lime);display:flex;align-items:center;justify-content:center}
.header-rule{position:absolute;left:0;right:0;top:61px;border-top:1px dashed #ccc}
.main-nav{position:absolute;top:71px;left:0;right:0;display:flex;justify-content:center;gap:24px;font-size:12px;color:#222}
.main-nav .active{color:var(--red)}

/* hero */
.hero{height:354px}
.hero svg{display:block}
.hero-label{font-weight:700;font-size:23px;fill:var(--label)}

/* suffering */
.suffering{height:283px;background:linear-gradient(180deg,#2b9a3a,#2d8f36 60%,#3c9a3c)}
.suffering h2{position:absolute;top:20px;left:0;right:0;text-align:center;color:var(--white);font-size:33px;font-weight:600}
.ailments{position:absolute;top:72px;left:0;right:0;display:flex}
.ailments ul{width:178px;color:var(--white);font-size:11px;font-weight:600}
.ailments li{position:relative;padding-left:11px;margin-bottom:9.5px;line-height:1.25}
.ailments li::before{content:"";position:absolute;left:0;top:4px;width:3px;height:3px;border-radius:50%;background:var(--white)}

/* treat */
.treat{height:410px}
.leaf-area{position:absolute;border-radius:50%;background:radial-gradient(circle,rgba(90,180,60,.55),rgba(90,180,60,0) 70%)}
.treat-visual{position:absolute;left:34px;top:95px;width:200px;height:200px;border-radius:16px;transform:rotate(12deg);background:linear-gradient(160deg,#29b6e8,#1f88c9);box-shadow:0 6px 16px rgba(0,0,0,.15)}
.treat-frame{position:absolute;border:1.5px solid;border-radius:16px;transform:rotate(45deg)}
.treat-copy{position:absolute;left:297px;top:60px;width:400px}
.treat-copy h2{font-size:29px;font-weight:400;color:var(--red);line-height:1.05}
.treat-copy p{font-size:10.5px;line-height:1.5;margin-top:22px;width:395px}
.treat-lists{display:flex;margin-top:12px}
.treat-lists ul{width:169px;font-size:10.5px;color:#333}
.treat-lists li{position:relative;padding-left:18px;margin-bottom:9px}
.treat-lists li::before{content:"";position:absolute;left:3px;top:2px;width:5px;height:5px;border:1px solid #999;border-radius:50%}

/* services */
.services{height:604px;background:var(--gray);overflow:visible}
.services-band{position:absolute;left:0;top:0;width:100%;height:234px;background:linear-gradient(90deg,#86c12c,#3da137 55%,#1f8a37)}
.services h2{position:absolute;top:34px;left:0;right:0;text-align:center;color:var(--white);font-size:46px;font-weight:700}
.services-rule{position:absolute;top:82px;left:50%;margin-left:-32px;width:64px;height:2px;background:var(--white)}
.services-intro{position:absolute;top:104px;left:0;right:0;text-align:center;color:var(--white);font-size:11.5px;line-height:1.3;font-weight:600}
.cards{position:absolute;top:179px;left:0;right:0;display:flex;gap:18px}
.card{width:160px;height:366px;background:var(--white);border-radius:4px;box-shadow:0 2px 8px rgba(0,0,0,.1)}
.card-photo{height:82px;border-radius:4px 4px 0 0}
.card-body{padding:18px 17px 0 17px}
.card h3{font-size:16.5px;font-weight:400;color:var(--red);line-height:1.05;white-space:nowrap}
.card p{font-size:9px;line-height:1.5;margin-top:8px}
.card ul{margin-top:8px}
.card li{position:relative;padding-left:11px;font-size:9px;line-height:1.5;margin-bottom:4px}
.card li::before{content:"";position:absolute;left:1px;top:4px;width:3px;height:3px;border-radius:50%;background:#444}
.card .more{display:block;color:var(--green);font-size:10.5px;margin-top:16px}

/* info columns */
.info{height:255px}
.info-col{position:absolute;top:20px}
.info h3{font-size:16px;font-weight:700;color:var(--green);line-height:1.2}
.info-rule{width:56px;height:1px;background:#ccc;margin:6px 0 10px}
.info p{font-size:9.3px;line-height:1.45;margin-bottom:8px}
.info-lists{display:flex}
.info-lists ul{width:138px}
.info-lists li{position:relative;padding-left:11px;font-size:9.3px;margin-bottom:9px}
.info-lists li::before{content:"";position:absolute;left:0;top:3px;width:3px;height:3px;border-radius:50%;background:#444}

/* wealth */
.wealth{height:375px}
.corner{position:absolute;border-color:#bbb;border-style:solid;width:76px;height:40px}
.wealth h2{position:absolute;top:25px;left:0;right:0;text-align:center;font-size:31px;font-weight:700;color:var(--green);letter-spacing:.4px}
.wealth p{position:absolute;top:90px;left:50%;margin-left:-266px;width:532px;text-align:center;font-size:9.5px;line-height:2;color:#333}
.wealth p em{font-style:normal;color:var(--red)}
.btn-outline{position:absolute;top:185px;left:50%;margin-left:-66px;width:132px;height:32px;border:1.5px solid #bbb;border-radius:16px;display:flex;align-items:center;justify-content:center;font-size:11px;color:var(--green)}

/* footer */
.site-footer{height:244px;background:var(--green-dark);color:var(--white)}
.footer-col{position:absolute;top:24px}
.footer-col h4{font-size:15px;font-weight:400;margin-bottom:16px}
.footer-col li{font-size:9px;margin-bottom:10px;line-height:1.4}
.contact-row{display:flex;gap:12px;font-size:9.5px;line-height:1.35;margin-bottom:16px}
.contact-icon{width:20px;height:20px;border:1.2px solid var(--lime);border-radius:50%;flex:none;display:flex;align-items:center;justify-content:center}
.social{display:flex;gap:8px}
.social span{width:24px;height:24px;border:1.2px solid var(--lime);border-radius:50%}
.copyright{position:absolute;left:0;bottom:0;width:100%;height:33px;background:var(--green-deep);text-align:center;font-size:8.5px;line-height:33px;color:#cfe7c9}
</style>
</head>
<body>

<header class="site-header">
  <div class="wrap">
    <div class="brand">
      <div class="brand-mark"></div>
      <div>
        <div class="brand-doctor">Dr. Anita Verghese (MBBS, MD)</div>
        <div class="brand-name">VERDANT CARE HUB</div>
        <div class="brand-tag">Allopathy, Ayurveda, Homeopathy, Acupuncture/Sujok</div>
      </div>
    </div>
    <div class="header-phone">
      <span class="phone-box"><svg width="10" height="14" viewBox="0 0 10 14"><rect x="1" y="1" width="8" height="12" rx="1.5" fill="none" stroke="#fff" stroke-width="1.5"/><circle cx="5" cy="10.5" r=".9" fill="#fff"/></svg></span>
      9800 412 365, 8200 579 140
    </div>
    <div class="header-rule"></div>
    <nav class="main-nav">
      <span class="active">Home</span><span>About us</span><span>Services ⌄</span><span>Work with us</span><span>Videos</span><span>Contact us</span>
    </nav>
  </div>
</header>

<section class="hero">
  <svg width="1200" height="354" viewBox="0 0 1200 354">
    <defs>
      <linearGradient id="gNutri" x1="0" y1="0" x2="1" y2="1"><stop offset="0" stop-color="#6a3a6e"/><stop offset=".5" stop-color="#e0b32a"/><stop offset="1" stop-color="#6aa532"/></linearGradient>
      <linearGradient id="gVitc" x1="0" y1="0" x2="1" y2="1"><stop offset="0" stop-color="#f6a21c"/><stop offset="1" stop-color="#e8731a"/></linearGradient>
      <linearGradient id="gChel" x1="0" y1="0" x2="1" y2="1"><stop offset="0" stop-color="#e38a3c"/><stop offset=".6" stop-color="#8a3a2a"/><stop offset="1" stop-color="#3a1e1a"/></linearGradient>
      <linearGradient id="gHomeo" x1="0" y1="0" x2="1" y2="1"><stop offset="0" stop-color="#8a5a18"/><stop offset=".5" stop-color="#e0a22a"/><stop offset="1" stop-color="#f3efe8"/></linearGradient>
      <linearGradient id="gAcu" x1="0" y1="0" x2="1" y2="1"><stop offset="0" stop-color="#e2c7b3"/><stop offset="1" stop-color="#a88672"/></linearGradient>
      <linearGradient id="gAyur" x1="0" y1="0" x2="1" y2="1"><stop offset="0" stop-color="#6a4a34"/><stop offset=".6" stop-color="#c38a52"/><stop offset="1" stop-color="#5c4438"/></linearGradient>
    </defs>
    <rect width="1200" height="354" fill="#e9ecee"/>
    <g stroke="#fff" stroke-width="6">
      <polygon role="img" aria-label="IV nutrition infusion with fresh vegetables and grapes" points="75,0 285,0 240,151 30,151" fill="url(#gNutri)"/>
      <polygon role="img" aria-label="IV vitamin C infusion with halved oranges and kiwi" points="285,0 480,0 435,151 240,151" fill="url(#gVitc)"/>
      <polygon role="img" aria-label="Chelation IV therapy shown with an illustrated human heart" points="480,0 675,0 630,151 435,151" fill="url(#gChel)"/>
      <polygon role="img" aria-label="Amber homeopathy bottles" points="675,0 870,0 825,151 630,151" fill="url(#gHomeo)"/>
      <polygon role="img" aria-label="Acupuncture needle in skin" points="870,0 1070,0 1025,151 825,151" fill="url(#gAcu)"/>
      <polygon role="img" aria-label="Ayurveda candles and herbs" points="1070,0 1200,0 1200,151 1025,151" fill="url(#gAyur)"/>
      <polygon role="img" aria-label="Fresh fruit and grapes for IV nutrition" points="0,208 205,208 160,354 0,354" fill="url(#gNutri)"/>
      <polygon role="img" aria-label="Orange and lemon slices for vitamin C infusion" points="205,208 400,208 355,354 160,354" fill="url(#gVitc)"/>
      <polygon role="img" aria-label="Illustrated circulation diagram" points="400,208 595,208 550,354 355,354" fill="url(#gChel)"/>
      <polygon role="img" aria-label="Homeopathy pills and daisy" points="595,208 790,208 745,354 550,354" fill="#efece6"/>
      <polygon role="img" aria-label="Acupuncture treatment" points="790,208 990,208 945,354 745,354" fill="url(#gAcu)"/>
      <polygon role="img" aria-label="Ayurveda candle and mortar" points="990,208 1200,208 1200,354 945,354" fill="url(#gAyur)"/>
    </g>
    <rect x="0" y="151" width="1200" height="57" fill="#fff"/>
    <text class="hero-label" x="58" y="174">Nutrition</text>
    <text class="hero-label" x="95" y="196">therapy</text>
    <text class="hero-label" x="252" y="174">Vitamin C</text>
    <text class="hero-label" x="293" y="196">therapy</text>
    <text class="hero-label" x="445" y="174">Chelation</text>
    <text class="hero-label" x="489" y="196">therapy</text>
    <text class="hero-label" x="638" y="187">Homoepathy</text>
    <text class="hero-label" x="832" y="187">Accupuncture</text>
    <text class="hero-label" x="1054" y="187">Ayurveda</text>
  </svg>
</section>

<section class="suffering">
  <div class="wrap">
    <h2>Are you suffering from ?</h2>
    <div class="ailments">
      <ul><li>Cardio Vascular Diseaes</li><li>Menstrual Disorders</li><li>Stroke/Paralysis</li><li>Migraine</li><li>Acidity</li><li>Muscular and Joint Pain</li><li>Arthiritis</li><li>Obesity</li></ul>
      <ul><li>Astma</li><li>Parkinsonim</li><li>Back Ache</li><li>Prostrate Gland<br>Enlasrgement</li><li>Body Pain</li><li>Psoriasis</li><li>Cervical and Lumbar<br>Spondylosis</li></ul>
      <ul><li>Sciatica</li><li>Cramps</li><li>Sinsuitis</li><li>Disc slips and disc prolaps</li><li>Snoring</li><li>Fibroid</li><li>Stress</li></ul>
      <ul><li>Hypertension</li><li>Tennis Elbow</li><li>Insomnia</li><li>Thyroid Issues</li><li>Kidney</li><li>Disorders</li><li>Ulcer</li></ul>
    </div>
  </div>
</section>

<section class="treat">
  <div class="leaf-area" role="img" aria-label="Green leaves" style="right:-10px;top:0;width:130px;height:100px"></div>
  <div class="leaf-area" role="img" aria-label="Green leaves" style="left:-40px;top:310px;width:90px;height:100px"></div>
  <div class="wrap">
    <div class="treat-frame" style="left:20px;top:110px;width:170px;height:170px;border-color:#bfe3dc"></div>
    <div class="treat-frame" style="left:70px;top:150px;width:170px;height:170px;border-color:#f3c6c8"></div>
    <div class="leaf-area" role="img" aria-label="Soft green leaves behind the photo" style="left:90px;top:40px;width:130px;height:90px"></div>
    <div class="treat-visual" role="img" aria-label="Doctor in blue scrubs holding a stethoscope"></div>
    <div class="treat-copy">
      <h2>We treat holistically using a<br>combination of</h2>
      <p>We are a "No SURGERY" centre dedicated to treating various diseases without Surgery. We treat holistically using a combination of</p>
      <div class="treat-lists">
        <ul><li>Allopathy</li><li>Homeopathy</li><li>IV Nutrition Therapy</li><li>Accupunture / Sujok</li><li>Arterio Clearance Therapy</li><li>Marma Therapy</li></ul>
        <ul><li>Arterio Clearance Therapy</li><li>Ayurveda</li><li>Hijama Cupping Therapy</li><li>Yoga</li><li>Alternative Therapies</li></ul>
      </div>
    </div>
  </div>
</section>

<section class="services">
  <div class="services-band"></div>
  <div class="wrap">
    <h2>Services</h2>
    <div class="services-rule"></div>
    <p class="services-intro">Most of our treatments are through Intravenous Infusion. Intravenous (IV) infusion is a method of feeding<br>vitamins, minerals, and other natural substances directly into a patient's bloodstream.</p>
    <div class="cards">
      <article class="card">
        <div class="card-photo" role="img" aria-label="Red heart with stethoscope on orange" style="background:linear-gradient(180deg,#f57c12,#e8600e)"></div>
        <div class="card-body">
          <h3>Arterio Clearance<br>Therapy</h3>
          <p>This therapy helps you</p>
          <ul><li>To clear the blocks of you Heart</li><li>It increases your energy level and concentration levels</li><li>It Lowers the risk of heart attach and stroke</li><li>It will help in reducing Pain and swelling and inflammatio</li></ul>
          <span class="more">Read More</span>
        </div>
      </article>
      <article class="card">
        <div class="card-photo" role="img" aria-label="Oranges on a tree for IV nutrition" style="background:linear-gradient(160deg,#f4a51c,#4e7a22)"></div>
        <div class="card-body">
          <h3>IV Nutrition<br>Therapy</h3>
          <p>This is where various nutrients are injected to your body</p>
          <ul><li>It has anti cancer properties particularly good for cancer patients</li><li>Increases the quality of life</li><li>It fights off cancer cells</li><li>Particularly good for asthma patient</li></ul>
          <span class="more" style="margin-top:18px">Read More</span>
        </div>
      </article>
      <article class="card">
        <div class="card-photo" role="img" aria-label="Purple flowers and white pills" style="background:linear-gradient(160deg,#2b2233,#7a5aa8 55%,#d8d0c8)"></div>
        <div class="card-body">
          <h3>Homeopathy</h3>
          <p>Homeopathy is safe, effective and fast acting</p>
          <ul><li>It is a scientific and natural medicine</li><li>It helps build resistance</li><li>Cure for most common illnesses</li><li>No side effects</li></ul>
          <span class="more">Read More</span>
        </div>
      </article>
      <article class="card">
        <div class="card-photo" role="img" aria-label="Back massage therapy" style="background:linear-gradient(160deg,#c88a6a,#8a5a44)"></div>
        <div class="card-body">
          <h3>Accupunture/Sujok/Marma</h3>
          <p>These therapies are Particularly effective for the following treatment</p>
          <ul><li>Migraines</li><li>Prostrate glands enlargements, body pain</li><li>Cervical and lumbar spondylitis</li><li>Kidney disorders, muscular and joint pains, thyroid issues</li></ul>
          <span class="more">Read More</span>
        </div>
      </article>
    </div>
  </div>
</section>

<section class="info">
  <div class="wrap">
    <div class="info-col" style="left:0;width:160px">
      <h3>Do you ?</h3>
      <div class="info-rule"></div>
      <p>Want to avoid Heart surgery ?</p>
      <p>Prefer to use natural substance for healing</p>
      <p>Prefer to stay away from the bad effects of common drugs</p>
      <p>Want to live a healthy life ?</p>
      <p>Want an healthy heart ?</p>
    </div>
    <div class="info-col" style="left:178px;width:205px">
      <h3>Choose the natural way to<br>healing</h3>
      <div class="info-rule"></div>
      <p>Clean Your Heart Without Undergoing Complicated Surgeries</p>
      <p>Protect Yourself From The Side Effects Of Allopathic Medicines</p>
      <p>All Consultation Starting @ Just Rs 99/-</p>
      <p>Live Natural : Breath Natural : Treat Natural</p>
    </div>
    <div class="info-col" style="left:415px;width:280px">
      <h3>An integrative medical clinic - All on<br>one roof</h3>
      <div class="info-rule"></div>
      <div class="info-lists">
        <ul><li>Allopathy</li><li>Ayurveda</li><li>Homeopathy</li><li>Accupuncture/Sujok</li><li>Arterio Clearance Therap</li></ul>
        <ul><li>IV Nutrition Therapy</li><li>Marma Theraphy</li><li>Other alternative therapies</li></ul>
      </div>
    </div>
  </div>
</section>

<section class="wealth">
  <div class="leaf-area" role="img" aria-label="Green floral ornament" style="right:-10px;top:-50px;width:130px;height:190px"></div>
  <div class="leaf-area" role="img" aria-label="Green floral ornament" style="left:-20px;top:210px;width:140px;height:130px"></div>
  <div class="corner" style="left:313px;top:-5px;border-width:2px 0 0 2px"></div>
  <div class="corner" style="left:811px;top:205px;border-width:0 2px 2px 0"></div>
  <h2>The Greatest Wealth Is Health</h2>
  <p>We are a 'NO SURGERY' centre dedicated to treating various diseases without surgery. <em>VCH deals with all kinds of life style disease especially Cardio Vascular Diseases like heart attack, Angina, Blocks and paralysis.</em> A few of the other conditions that we treat using IV nutrition techniques include hypertension, Chronic Obstructive Pulmonary Disease, asthma, fibromyalgia, chronic fatigue syndrome, diabetes, hepatitis, and even the common cold.</p>
  <div class="btn-outline">More About us</div>
</section>

<footer class="site-footer">
  <div class="wrap">
    <div class="footer-col" style="left:0;width:215px">
      <h4>Address</h4>
      <div class="contact-row"><span class="contact-icon"><svg width="8" height="11" viewBox="0 0 8 11"><path d="M4 10.5C1.5 7 .5 5.5.5 4a3.5 3.5 0 017 0c0 1.5-1 3-3.5 6.5z" fill="none" stroke="#8cc63f"/><circle cx="4" cy="4" r="1.2" fill="#8cc63f"/></svg></span><span>Metro Pillar 312, Lakeview Church Road, Opp Harbour Grand Hotel, Palmgrove, Kochi: 682099</span></div>
      <div class="contact-row" style="font-size:11px"><span class="contact-icon"><svg width="7" height="10" viewBox="0 0 7 10"><rect x=".6" y=".6" width="5.8" height="8.8" rx="1" fill="none" stroke="#8cc63f"/></svg></span><span>9800 412 365<br>8200 579 140</span></div>
      <div class="contact-row"><span class="contact-icon"><svg width="10" height="8" viewBox="0 0 10 8"><rect x=".5" y=".5" width="9" height="7" fill="none" stroke="#8cc63f"/><path d="M.5 .5L5 4.5 9.5 .5" fill="none" stroke="#8cc63f"/></svg></span><span style="line-height:20px">hello@verdantcarehub.in</span></div>
    </div>
    <div class="footer-col" style="left:237px">
      <h4>Usefull Links</h4>
      <ul><li>Home</li><li>About us</li><li>Work with us</li><li>Contact us</li></ul>
    </div>
    <div class="footer-col" style="left:356px;width:150px">
      <h4>Our Services</h4>
      <ul><li>Arterio Clearance Therapy</li><li>IV Nutrition Therapy</li><li>Homeopathy</li><li>Accupuncture/Sujok</li><li>Marma and Hijama Cupping Therapy</li><li>Yoga and Mediation</li></ul>
    </div>
    <div class="footer-col" style="left:534px">
      <h4>Follow Us</h4>
      <div class="social"><span></span><span></span><span></span></div>
    </div>
  </div>
  <div class="copyright">Copyright © 2019 www.verdantcarehub.in. All rights reserved</div>
</footer>

</body>
</html>
```